I need a book cover for a 6x9 book. The front cover information (title and author) is below, and the back cover information will be given to the winning designer. I am wanting something vibrant and bright, and I am open to your creativity, but I do not want any pictures of people on the cover. Save room for the barcode on the back cover.
Title:
Oops! Wrong Turn?
Quiet Rooms Explained: Notes on Patient Gardening Habits
Author:
Marisol Tembe

```html
<!DOCTYPE html>
<html lang="en">
<head>
<meta charset="utf-8">
<title>Oops! Wrong Turn? — Marisol Tembe</title>
<link rel="stylesheet" href="https://fonts.googleapis.com/css2?family=Roboto:wght@500;900&family=Roboto+Condensed:wght@400&display=swap">
<style>
  :root {
    --paper: #f7f6f4;
    --ink: #1c1c1c;
    --sky: #00b9ff;
    --white: #ffffff;
    --art-light: #ffffff;
    --art-shade: #e4e3e0;
  }
  * { margin: 0; padding: 0; box-sizing: border-box; }
  html, body { width: 800px; height: 1200px; overflow: hidden; background: var(--paper); }
  .cover {
    position: relative;
    width: 800px;
    height: 1200px;
    background: var(--paper);
    overflow: hidden;
    font-family: "Roboto", Arial, sans-serif;
  }
  .speech-art {
    position: absolute;
    left: 64px;
    top: 92px;
    width: 688px;
    height: 228px;
    border-radius: 40px;
    background: radial-gradient(ellipse at 50% 45%, var(--art-light) 0%, var(--art-light) 45%, var(--art-shade) 100%);
  }
  .title-line {
    position: absolute;
    left: 0;
    width: 800px;
    text-align: center;
    font-weight: 900;
    line-height: 1;
    white-space: nowrap;
    color: var(--ink);
    letter-spacing: -1px;
  }
  .title-line--first { top: 344px; font-size: 197px; }
  .title-line--second { top: 559px; font-size: 158px; }
  .title-line--third { top: 744px; font-size: 197px; color: var(--sky); }
  .divider {
    position: absolute;
    left: 179px;
    width: 452px;
    height: 3px;
    background: linear-gradient(90deg, rgba(28,28,28,0) 0%, var(--ink) 35%, var(--ink) 65%, rgba(28,28,28,0) 100%);
  }
  .divider--top { top: 959px; }
  .divider--bottom { top: 1077px; }
  .subtitle {
    position: absolute;
    left: 0;
    top: 972px;
    width: 800px;
    text-align: center;
    font-family: "Roboto Condensed", "Arial Narrow", sans-serif;
    font-weight: 400;
    font-size: 44px;
    line-height: 42px;
    color: var(--ink);
  }
  .subtitle__accent { display: block; color: var(--sky); }
  .author-band {
    position: absolute;
    left: 0;
    top: 1118px;
    width: 800px;
    height: 82px;
    background: var(--sky);
    display: flex;
    align-items: center;
    justify-content: center;
  }
  .author-name {
    font-family: "Roboto", Arial, sans-serif;
    font-weight: 500;
    font-size: 39px;
    letter-spacing: 4px;
    color: var(--white);
    text-transform: uppercase;
  }
</style>
</head>
<body>
  <main class="cover">
    <div class="speech-art" role="img" aria-label="Comic-style speech and thought bubbles with halftone shadows and a small star"></div>

    <h1 class="title">
      <span class="title-line title-line--first">OOPS!</span>
      <span class="title-line title-line--second">WRONG</span>
      <span class="title-line title-line--third">TURN?</span>
    </h1>

    <div class="divider divider--top"></div>
    <p class="subtitle">Quiet Rooms Explained: Notes on<span class="subtitle__accent">Patient Gardening Habits</span></p>
    <div class="divider divider--bottom"></div>

    <footer class="author-band">
      <p class="author-name">Marisol Tembe</p>
    </footer>
  </main>
</body>
</html>
```